we are a small based family business that specialise in 12v led lights for tarvin caravans.
we also sell 12v switches, wire, circuit breakers, dimmers etc but our main line is LEDs.
We would like something that reflects the LED lighting on our cards.
www.reefcrestlamps.example.au is where you can have a look at to get ideas, of our product.
I have attached the logo we generally use on all our shopra listings and is the main header on our website.

Look forward to seeing what your team comes up with.

Business

Tam 0491 738 205
Corrawin Vale QLD 4391

www.reefcrestlamps.example

```html
<!DOCTYPE html>
<html lang="en">
<head>
<meta charset="utf-8">
<title>Reef Crest Lamps — Business Card</title>
<link href="https://fonts.googleapis.com/css2?family=Cinzel:wght@400&family=Oswald:wght@700&display=swap" rel="stylesheet">
<style>
  :root {
    --backdrop-light: #f4f4f4;
    --backdrop-dark: #c9c9c9;
    --card-white: #f7f6f6;
    --panel-red-top: #9a1c22;
    --panel-red-bottom: #4e1216;
    --contact-ink: #d8a9a3;
    --brand-red: #a3161c;
    --bulb-tone: #ddbdb2;
  }
  html, body {
    margin: 0;
    width: 1200px;
    height: 1000px;
    overflow: hidden;
  }
  body {
    background: radial-gradient(ellipse at 55% 45%, var(--backdrop-light) 0%, #e6e6e6 55%, var(--backdrop-dark) 100%);
    position: relative;
  }
  .business-card {
    position: absolute;
    left: 180px;
    top: 260px;
    width: 840px;
    height: 480px;
    display: flex;
    background: var(--card-white);
    box-shadow: 0 14px 34px rgba(0,0,0,0.22);
  }
  .contact-panel {
    position: relative;
    width: 460px;
    height: 100%;
    background: linear-gradient(160deg, var(--panel-red-top) 0%, #7a171c 45%, var(--panel-red-bottom) 100%);
  }
  .contact-details {
    position: absolute;
    left: 36px;
    top: 262px;
    margin: 0;
    font-family: "Cinzel", serif;
    font-size: 17px;
    letter-spacing: 1.5px;
    line-height: 30px;
    color: var(--contact-ink);
  }
  .contact-line { display: block; }
  .web-line {
    display: flex;
    align-items: center;
    gap: 10px;
    margin-top: 16px;
  }
  .web-icon { width: 20px; height: 20px; }
  .brand-panel {
    position: relative;
    flex: 1;
  }
  .brand-name {
    position: absolute;
    right: 30px;
    top: 44px;
    margin: 0;
    font-family: "Oswald", sans-serif;
    font-weight: 700;
    font-size: 42px;
    line-height: 1;
    letter-spacing: 0.5px;
    color: var(--brand-red);
    text-transform: uppercase;
  }
  .bulb-artwork {
    position: absolute;
    left: 120px;
    top: 190px;
    width: 140px;
    height: 230px;
    border-radius: 40% 40% 48% 48% / 22% 22% 40% 40%;
    background: var(--bulb-tone);
  }
</style>
</head>
<body>
  <section class="business-card">
    <div class="contact-panel">
      <p class="contact-details">
        <span class="contact-line">Tam 0491 738 205 Corrawin Vale</span>
        <span class="contact-line">QLD 4391</span>
        <span class="contact-line web-line">
          <svg class="web-icon" viewBox="0 0 20 20" aria-hidden="true">
            <g fill="none" stroke="var(--contact-ink)" stroke-width="1.4">
              <circle cx="10" cy="10" r="8"/>
              <ellipse cx="10" cy="10" rx="3.5" ry="8"/>
              <line x1="2" y1="10" x2="18" y2="10"/>
            </g>
          </svg>
          www.reefcrestlamps.example
        </span>
      </p>
    </div>
    <div class="brand-panel">
      <h1 class="brand-name">Reef Crest Lamps</h1>
      <div class="bulb-artwork" role="img" aria-label="Illustration of a light bulb in soft blush tone"></div>
    </div>
  </section>
</body>
</html>
```